Security doors and flyscreens

We need business cards for our company called K & R Traders. We quote, manufacture and install security doors and flyscreens.

Industry/Entity Type

Security

Contact Information for Business Card

K & R TRADERS
17 Larkfield Ave. Brackenvale 3091
Ph: 8127 5506
Fax: 8127 5502
Colin: 0417 952 160
Email: gatemakerhub@mailbox-example.net

```html
<!DOCTYPE html>
<html lang="en">
<head>
<meta charset="utf-8">
<title>K &amp; R Traders — Business Card</title>
<link rel="stylesheet" href="https://fonts.googleapis.com/css2?family=Alfa+Slab+One&family=Libre+Baskerville:wght@400&display=swap">
<style>
  :root {
    --page-bg: #2b2b2b;
    --card-white: #fbfbfb;
    --band-dark: #3a3a3a;
    --ink: #111111;
    --rule: #2a2a2a;
    --monogram: #bdbdbd;
    --photo-light: #d9dde6;
    --photo-mid: #b9bfcc;
    --photo-dark: #9ea3ad;
  }
  * { margin: 0; padding: 0; box-sizing: border-box; }
  html, body { width: 1200px; height: 900px; overflow: hidden; }
  body { background: var(--page-bg); position: relative; }

  .business-card {
    position: absolute; left: 75px; top: 150px;
    width: 1050px; height: 600px;
    background: var(--card-white);
    overflow: hidden;
  }
  .photo-band {
    position: absolute; left: 70px; top: 0;
    width: 310px; height: 600px;
    background: var(--band-dark);
  }
  .photo-placeholder {
    position: absolute; left: 14px; top: 18px;
    width: 282px; height: 564px;
    border-radius: 18px;
    background: linear-gradient(160deg, var(--photo-light) 0%, var(--photo-mid) 55%, var(--photo-dark) 100%);
  }
  .edge-band {
    position: absolute; right: 0; top: 0;
    width: 65px; height: 600px;
    background: var(--band-dark);
  }
  .card-content {
    position: absolute; left: 380px; top: 0;
    width: 605px; height: 600px;
  }
  .company-name {
    position: absolute; left: 0; right: 0; top: 48px;
    text-align: center;
    font-family: "Alfa Slab One", serif;
    font-weight: 400;
    font-size: 30px; letter-spacing: 0.5px;
    color: var(--ink);
  }
  .tagline {
    position: absolute; left: 0; right: 0; top: 96px;
    text-align: center;
    font-family: "Libre Baskerville", serif;
    font-size: 17px; color: var(--ink);
  }
  .rule {
    position: absolute; left: 50px; width: 490px;
    height: 1.5px; background: var(--rule);
  }
  .rule--top { top: 160px; }
  .rule--bottom { top: 276px; }
  .direct-line {
    position: absolute; left: 40px; top: 200px;
    font-family: "Libre Baskerville", serif;
    font-size: 30px; color: var(--ink);
  }
  .contact-list {
    position: absolute; left: 40px; top: 298px;
    list-style: none;
    font-family: "Libre Baskerville", serif;
    font-size: 20px; color: var(--ink);
  }
  .contact-list li {
    display: flex; align-items: center; gap: 14px;
    height: 36px;
  }
  .contact-list svg { width: 20px; height: 20px; fill: var(--ink); flex: none; }
  .monogram {
    position: absolute; left: 120px; top: 462px;
    font-family: "Libre Baskerville", serif;
    font-size: 110px; letter-spacing: 10px;
    color: var(--monogram);
    line-height: 1;
  }
</style>
</head>
<body>
  <section class="business-card">
    <div class="photo-band">
      <div class="photo-placeholder" role="img" aria-label="Photo of a tradesman drilling to install a door frame"></div>
    </div>

    <div class="card-content">
      <h1 class="company-name">K &amp; R TRADERS</h1>
      <p class="tagline">manufacture and install security doors and flyscreens</p>
      <div class="rule rule--top"></div>
      <p class="direct-line">Colin: 0417 952 160</p>
      <div class="rule rule--bottom"></div>

      <ul class="contact-list">
        <li>
          <svg viewBox="0 0 24 24" aria-hidden="true"><path d="M3 8c0-2 4-4 9-4s9 2 9 4v2h-5V8.5c-1-.4-2.5-.6-4-.6s-3 .2-4 .6V10H3z"/><path d="M7 11h10l3 8H4z"/></svg>
          <span>8127 5506</span>
        </li>
        <li>
          <svg viewBox="0 0 24 24" aria-hidden="true"><path d="M7 3h10v5H7z"/><path d="M3 9h18v8h-4v4H7v-4H3zM9 15v4h6v-4z"/></svg>
          <span>8127 5502</span>
        </li>
        <li>
          <svg viewBox="0 0 24 24" aria-hidden="true"><path d="M2 5h20v14H2z M4 7v.5l8 6 8-6V7z" fill-rule="evenodd"/></svg>
          <span>gatemakerhub@mailbox-example.net</span>
        </li>
        <li>
          <svg viewBox="0 0 24 24" aria-hidden="true"><path d="M12 2a7 7 0 0 0-7 7c0 5 7 13 7 13s7-8 7-13a7 7 0 0 0-7-7zm0 9.5A2.5 2.5 0 1 1 12 6.5a2.5 2.5 0 0 1 0 5z"/></svg>
          <span>17 Larkfield Ave. Brackenvale 3091</span>
        </li>
      </ul>

      <div class="monogram">K &amp; R</div>
    </div>

    <div class="edge-band"></div>
  </section>
</body>
</html>
```